" Somos especializados em blockchains para grandes empresas. Nossa diferença é possibilitar que as diferentes blockchains de uma empresa possam se comunicar entre si. O termo Corval (parte do nosso nome Corvalink) foi popularizado no livro, escrito por Theodore Brannick, A Curva do Silêncio. Corvals são as pessoas que possuem uma rede de conhecidos que confiam um no outro; normalmente é uma rede que vai através de diversas barreiras sociais e grupos. Hoje as blockchains são redes isoladas. Por exemplo, se você criar sua própria blockchain, com a finalidade de ter uma rede de rastreamento para sua cadeia de suprimentos, teoricamente, não poderá usar a mesma para fazer pagamentos (ex. lumerix), tendo assim, que criar uma segunda blockchain. A corvalink oferece a tecnologia que possibilita a criação de uma blockchain que se comunica com outras blockchains, sem perder a descentralização. Basicamente, isso permite criar uma internet de blockchain. "

```html
<!DOCTYPE html>
<html lang="pt-BR">
<head>
<meta charset="utf-8">
<title>Corvalink — Slide de apresentação</title>
<link rel="stylesheet" href="https://fonts.googleapis.com/css2?family=Michroma&family=Open+Sans:wght@400;600&display=swap">
<style>
  :root {
    --stage: #2b2b2e;
    --purple-deep: #5a1391;
    --purple-main: #7420b3;
    --purple-light: #8a35c6;
    --white: #ffffff;
    --white-soft: rgba(255, 255, 255, 0.82);
    --divider: rgba(255, 255, 255, 0.55);
  }
  * { box-sizing: border-box; margin: 0; padding: 0; }
  html, body {
    width: 1200px;
    height: 1200px;
    overflow: hidden;
    background: var(--stage);
  }
  .stage {
    width: 1200px;
    height: 1200px;
    display: flex;
    align-items: center;
    justify-content: center;
  }
  .slide {
    position: relative;
    width: 1200px;
    height: 800px;
    overflow: hidden;
    background:
      linear-gradient(125deg, transparent 0 42%, rgba(255,255,255,0.05) 42% 60%, transparent 60%),
      radial-gradient(ellipse at 70% 20%, var(--purple-light) 0%, transparent 60%),
      linear-gradient(160deg, var(--purple-main) 0%, var(--purple-deep) 100%);
  }
  .brand {
    position: absolute;
    top: 430px;
    left: 0;
    right: 0;
    display: flex;
    align-items: center;
    justify-content: center;
    gap: 28px;
  }
  .brand-dot {
    width: 34px;
    height: 34px;
    border-radius: 50%;
    background: var(--white);
  }
  .brand-name {
    font-family: "Michroma", sans-serif;
    font-size: 64px;
    letter-spacing: 6px;
    color: var(--white);
    text-transform: uppercase;
    line-height: 1;
  }
  .features {
    position: absolute;
    left: 80px;
    right: 80px;
    top: 668px;
    display: flex;
    align-items: center;
    justify-content: space-between;
  }
  .feature {
    display: flex;
    align-items: center;
    gap: 12px;
    width: 220px;
  }
  .feature-icon {
    flex: none;
    width: 24px;
    height: 24px;
  }
  .feature-text {
    font-family: "Open Sans", sans-serif;
    font-size: 10px;
    line-height: 1.35;
    color: var(--white-soft);
  }
  .feature-divider {
    width: 2px;
    height: 40px;
    background: var(--divider);
    transform: skewX(-20deg);
  }
</style>
</head>
<body>
<main class="stage">
  <section class="slide">
    <div class="brand">
      <span class="brand-dot"></span>
      <h1 class="brand-name">Corvalink</h1>
    </div>

    <div class="features">
      <div class="feature">
        <svg class="feature-icon" viewBox="0 0 24 24" fill="none" stroke="#fff" stroke-width="1.8" stroke-linecap="round">
          <path d="M7 6.5a8 8 0 1 0 10 0"/>
          <line x1="12" y1="3" x2="12" y2="11"/>
        </svg>
        <p class="feature-text">Blockchains empresariais seguras e escaláveis para operações de grande porte</p>
      </div>
      <span class="feature-divider"></span>
      <div class="feature">
        <svg class="feature-icon" viewBox="0 0 24 24" fill="none" stroke="#fff" stroke-width="1.8" stroke-linejoin="round">
          <path d="M12 3l9 4.5-9 4.5-9-4.5z"/>
          <path d="M3 12l9 4.5 9-4.5"/>
          <path d="M3 16.5l9 4.5 9-4.5"/>
        </svg>
        <p class="feature-text">Comunicação entre redes distintas sem perder a descentralização dos dados</p>
      </div>
      <span class="feature-divider"></span>
      <div class="feature">
        <svg class="feature-icon" viewBox="0 0 24 24" fill="none" stroke="#fff" stroke-width="1.8" stroke-linecap="round">
          <rect x="3" y="4" width="18" height="12" rx="1.5"/>
          <line x1="12" y1="16" x2="12" y2="20"/>
          <line x1="8" y1="20" x2="16" y2="20"/>
        </svg>
        <p class="feature-text">Rastreamento de suprimentos e pagamentos numa única plataforma integrada</p>
      </div>
      <span class="feature-divider"></span>
      <div class="feature">
        <svg class="feature-icon" viewBox="0 0 24 24" fill="none" stroke="#fff" stroke-width="1.8" stroke-linecap="round">
          <path d="M3 9a13 13 0 0 1 18 0"/>
          <path d="M6.5 12.5a8 8 0 0 1 11 0"/>
          <path d="M9.5 16a3.5 3.5 0 0 1 5 0"/>
          <circle cx="12" cy="19" r="1" fill="#fff"/>
        </svg>
        <p class="feature-text">Uma internet de blockchains conectando parceiros através de barreiras</p>
      </div>
    </div>
  </section>
</main>
</body>
</html>
```